Smile club flyer design

I am launching an office smile club and would like a design that sits my branding and that is appealing to customers. I have a design (I need a new one) that has all the information.
My website is maplecrestdentalcaretn.example
Brand color is green. The design can be any color

Target Market(s)

Ages 30+

Industry/Entity Type

Dental

Font styles to use
Serif

Requirements
Must have
• Appealing to patients

```html
<!DOCTYPE html>
<html lang="en">
<head>
<meta charset="utf-8">
<title>Maplecrest Dental Care – Smile Club Membership</title>
<link href="https://fonts.googleapis.com/css2?family=Montserrat:wght@500;600;700;800&family=Oswald:wght@500;600&family=Roboto+Condensed:wght@500;600&family=Kaushan+Script&family=Libre+Baskerville:wght@400&display=swap" rel="stylesheet">
<style>
  :root{
    --backdrop:#272727;
    --green:#0b8a3e;
    --green-deep:#086b2f;
    --lime:#9bde4d;
    --lime-pale:#c8ef9f;
    --white:#ffffff;
    --ink:#1d2a1f;
  }
  *{box-sizing:border-box;margin:0;padding:0}
  html,body{width:956px;height:1200px;overflow:hidden;background:var(--backdrop)}
  .flyer{position:absolute;left:165px;top:139px;width:627px;height:940px;overflow:hidden;
    background:linear-gradient(180deg,#f7fbef 0%,#eef8e2 30%,#e3f4cf 55%,#d9f0bf 100%);
    font-family:"Montserrat",sans-serif;color:var(--ink)}
  .bg-shapes{position:absolute;inset:0}
  .smile-photo{position:absolute;left:336px;top:48px;width:291px;height:300px;
    border-radius:45% 0 0 30%/40% 0 0 30%;
    background:radial-gradient(ellipse at 55% 55%,#f4f1ec 0%,#e9b49b 25%,#d98f77 45%,#e8b39c 70%,#f1cfbd 100%)}
  .brand{position:absolute;left:448px;top:26px;width:170px;text-align:center;color:var(--white)}
  .brand-name{font-family:"Libre Baskerville",serif;font-size:23px;line-height:1}
  .brand-sub{font-family:"Libre Baskerville",serif;font-size:9px;letter-spacing:3px;margin-top:4px}
  .intro{position:absolute;left:41px;top:36px;font-family:"Kaushan Script",cursive;font-size:32px;line-height:1.1;color:#5bbf2a}
  .headline{position:absolute;left:40px;top:82px;font-weight:800;line-height:.98;letter-spacing:-1px}
  .headline .l1{font-size:47px;color:var(--green)}
  .headline .l2{font-size:43px;color:var(--green-deep)}
  .tag-bar{position:absolute;left:42px;top:187px;width:4px;height:53px;background:var(--green)}
  .pill{position:absolute;height:32px;border-radius:16px;display:flex;align-items:center;justify-content:center;
    font-weight:600;white-space:nowrap}
  .tag-outline{left:53px;top:179px;width:266px;background:var(--white);border:2px solid var(--lime);color:var(--green);font-size:16px}
  .tag-solid{left:53px;top:213px;width:266px;background:var(--green);border:2px solid var(--lime);color:var(--white);font-size:16px;justify-content:flex-start;padding-left:15px}
  .card{position:absolute;width:182px;height:248px;background:var(--white);border-radius:10px;
    box-shadow:0 3px 10px rgba(40,90,20,.15)}
  .card::after{content:"";position:absolute;left:0;right:0;top:215px;height:2px;background:var(--lime)}
  .features{position:absolute;left:16px;right:10px;top:100px;list-style:none;
    font-family:"Roboto Condensed",sans-serif;font-weight:500;font-size:12px;line-height:15px}
  .features li{position:relative;padding-left:15px;margin-bottom:5px}
  .features li svg{position:absolute;left:0;top:2px;width:11px;height:11px}
  .price-pill{position:absolute;width:141px;height:32px;border-radius:16px;background:var(--green);border:2px solid var(--lime);
    color:var(--white);font-size:17px;font-weight:600;display:flex;align-items:center;justify-content:center}
  .arc{position:absolute;width:170px;height:62px}
  .badge{position:absolute;width:140px;height:140px;border-radius:50%;background:var(--green);
    box-shadow:0 8px 0 0 var(--lime);color:var(--white);text-align:center;display:flex;flex-direction:column;justify-content:center;align-items:center}
  .badge-title{font-family:"Oswald",sans-serif;font-weight:600;font-size:24px;line-height:1}
  .badge-sub{font-size:9px;font-weight:500;margin:3px 0 2px;letter-spacing:.3px}
  .badge-price{font-family:"Oswald",sans-serif;font-weight:600;font-size:38px;line-height:1.05}
  .badge-per{font-size:8px;font-weight:500}
  .offer-card{position:absolute;left:417px;top:694px;width:183px;height:170px;background:var(--green);border-radius:8px 8px 0 0}
  .offer-card::after{content:"";position:absolute;left:0;right:0;top:131px;height:2px;background:var(--lime)}
  .offer-card .features{top:92px;color:var(--white)}
  .badge-new{font-family:"Kaushan Script",cursive;font-size:20px;line-height:1.1}
  .badge-smile{font-weight:800;font-size:26px;line-height:1}
  .offer-pill{left:430px;top:839px;width:159px;background:var(--white);border:2px solid var(--lime);color:var(--green);font-size:12px;font-weight:700}
  .join{position:absolute;left:0;top:737px;width:418px;height:88px;background:var(--lime)}
  .join-title{position:absolute;left:24px;top:13px;font-size:27px;font-weight:800;color:var(--white);letter-spacing:-.5px;
    text-shadow:1px 1px 0 #3a6d1e,2px 2px 2px rgba(0,0,0,.35)}
  .join-phone{position:absolute;left:58px;top:47px;font-size:27px;font-weight:800;color:var(--white);
    text-shadow:1px 1px 0 #3a6d1e,2px 2px 2px rgba(0,0,0,.35)}
  .phone-icon{position:absolute;left:21px;top:50px;width:27px;height:27px}
  .finance-title{position:absolute;left:21px;top:837px;font-size:16px;font-weight:600;color:var(--green-deep)}
  .partner{position:absolute;top:863px;font-size:19px;font-weight:700;color:var(--green-deep);display:flex;align-items:center;gap:6px;white-space:nowrap}
  .partner .dot{width:12px;height:12px;border-radius:50%;background:var(--green-deep)}
  .partner-a{left:21px}
  .partner-b{left:180px}
  .plans{position:absolute;left:383px;top:888px;font-size:14px;font-weight:600;color:var(--ink)}
  .fee-band{position:absolute;left:0;top:910px;width:627px;height:30px}
  .fee-text{position:absolute;right:26px;top:912px;font-family:"Roboto Condensed",sans-serif;font-weight:600;font-size:17px;color:var(--white)}
</style>
</head>
<body>
<main class="flyer">

  <svg class="bg-shapes" viewBox="0 0 627 940" width="627" height="940" aria-hidden="true">
    <path d="M0,212 C150,330 320,390 627,300 L627,316 C330,410 150,390 0,286 Z" fill="var(--lime)"/>
    <path d="M0,286 C150,390 330,410 627,316 L627,332 C340,450 120,430 0,348 Z" fill="var(--green)"/>
  </svg>

  <div class="smile-photo" role="img" aria-label="Close-up photo of a smiling mouth showing white teeth"></div>

  <svg class="bg-shapes" viewBox="0 0 627 940" width="627" height="940" aria-hidden="true">
    <path d="M305,0 C380,110 500,140 627,122 L627,130 C490,148 370,115 290,0 Z" fill="var(--lime-pale)"/>
    <path d="M360,0 C430,95 520,125 627,118 L627,112 C540,110 470,70 420,0 Z" fill="var(--lime)"/>
    <path d="M405,0 L627,0 L627,112 C540,112 460,72 405,0 Z" fill="var(--green)"/>
  </svg>

  <div class="brand">
    <div class="brand-name">Maplecrest</div>
    <div class="brand-sub">— DENTAL CARE —</div>
  </div>

  <div class="intro">Introducing</div>
  <h1 class="headline"><span class="l1">SMILE CLUB</span><br><span class="l2">MEMBERSHIP</span></h1>
  <div class="tag-bar"></div>
  <div class="pill tag-outline">AFFORDABLE DENTAL CARE</div>
  <div class="pill tag-solid">NO INSURANCE REQUIRED</div>

  <!-- Core Care -->
  <section class="card" style="left:26px;top:445px">
    <ul class="features">
      <li><svg viewBox="0 0 12 12"><circle cx="6" cy="6" r="6" fill="#0b8a3e"/><path d="M3.2 6.2l1.9 1.8 3.7-3.8" stroke="#fff" stroke-width="1.6" fill="none"/></svg>Comprehensive Annual Exam</li>
      <li><svg viewBox="0 0 12 12"><circle cx="6" cy="6" r="6" fill="#0b8a3e"/><path d="M3.2 6.2l1.9 1.8 3.7-3.8" stroke="#fff" stroke-width="1.6" fill="none"/></svg>2 Professional Cleanings<br>per Year</li>
      <li><svg viewBox="0 0 12 12"><circle cx="6" cy="6" r="6" fill="#0b8a3e"/><path d="M3.2 6.2l1.9 1.8 3.7-3.8" stroke="#fff" stroke-width="1.6" fill="none"/></svg>Routine Bitewing X-rays</li>
      <li><svg viewBox="0 0 12 12"><circle cx="6" cy="6" r="6" fill="#0b8a3e"/><path d="M3.2 6.2l1.9 1.8 3.7-3.8" stroke="#fff" stroke-width="1.6" fill="none"/></svg>10% Savings on Treatment</li>
    </ul>
  </section>
  <svg class="arc" style="left:32px;top:365px" viewBox="0 0 170 62" aria-hidden="true"><path d="M13,55 A78,78 0 0 1 157,55" stroke="var(--green)" stroke-width="2" fill="none"/><circle cx="13" cy="55" r="3.5" fill="var(--green)"/><circle cx="157" cy="55" r="3.5" fill="var(--green)"/></svg>
  <div class="badge" style="left:47px;top:380px">
    <div class="badge-title">CORE CARE</div><div class="badge-sub">PREVENTIVE</div>
    <div class="badge-price">$39</div><div class="badge-per">/MONTH</div>
  </div>
  <div class="price-pill" style="left:46px;top:674px">$39/MONTH</div>

  <!-- Bright -->
  <section class="card" style="left:222px;top:384px">
    <ul class="features">
      <li><svg viewBox="0 0 12 12"><circle cx="6" cy="6" r="6" fill="#0b8a3e"/><path d="M3.2 6.2l1.9 1.8 3.7-3.8" stroke="#fff" stroke-width="1.6" fill="none"/></svg>Annual In-Office Whitening (Top &amp; Bottom)</li>
      <li><svg viewBox="0 0 12 12"><circle cx="6" cy="6" r="6" fill="#0b8a3e"/><path d="M3.2 6.2l1.9 1.8 3.7-3.8" stroke="#fff" stroke-width="1.6" fill="none"/></svg>Custom Whitening Trays</li>
      <li><svg viewBox="0 0 12 12"><circle cx="6" cy="6" r="6" fill="#0b8a3e"/><path d="M3.2 6.2l1.9 1.8 3.7-3.8" stroke="#fff" stroke-width="1.6" fill="none"/></svg>15% Savings on Elective Treatment</li>
    </ul>
  </section>
  <svg class="arc" style="left:228px;top:301px" viewBox="0 0 170 62" aria-hidden="true"><path d="M13,55 A78,78 0 0 1 157,55" stroke="var(--green)" stroke-width="2" fill="none"/><circle cx="13" cy="55" r="3.5" fill="var(--green)"/><circle cx="157" cy="55" r="3.5" fill="var(--green)"/></svg>
  <div class="badge" style="left:243px;top:316px">
    <div class="badge-title">BRIGHT</div><div class="badge-sub">COSMETIC</div>
    <div class="badge-price">$59</div><div class="badge-per">/MONTH</div>
  </div>
  <div class="price-pill" style="left:243px;top:613px">$59/MONTH</div>

  <!-- Total Smile -->
  <section class="card" style="left:417px;top:342px">
    <ul class="features">
      <li><svg viewBox="0 0 12 12"><circle cx="6" cy="6" r="6" fill="#0b8a3e"/><path d="M3.2 6.2l1.9 1.8 3.7-3.8" stroke="#fff" stroke-width="1.6" fill="none"/></svg>3-4 Perio Maintenance Visits per Year</li>
      <li><svg viewBox="0 0 12 12"><circle cx="6" cy="6" r="6" fill="#0b8a3e"/><path d="M3.2 6.2l1.9 1.8 3.7-3.8" stroke="#fff" stroke-width="1.6" fill="none"/></svg>1 Comprehensive Exam</li>
      <li><svg viewBox="0 0 12 12"><circle cx="6" cy="6" r="6" fill="#0b8a3e"/><path d="M3.2 6.2l1.9 1.8 3.7-3.8" stroke="#fff" stroke-width="1.6" fill="none"/></svg>Diagnostic X-rays</li>
      <li><svg viewBox="0 0 12 12"><circle cx="6" cy="6" r="6" fill="#0b8a3e"/><path d="M3.2 6.2l1.9 1.8 3.7-3.8" stroke="#fff" stroke-width="1.6" fill="none"/></svg>15% Savings on Restorative &amp; Elective Care</li>
    </ul>
  </section>
  <svg class="arc" style="left:425px;top:260px" viewBox="0 0 170 62" aria-hidden="true"><path d="M13,55 A78,78 0 0 1 157,55" stroke="var(--green)" stroke-width="2" fill="none"/><circle cx="13" cy="55" r="3.5" fill="var(--green)"/><circle cx="157" cy="55" r="3.5" fill="var(--green)"/></svg>
  <div class="badge" style="left:440px;top:275px">
    <div class="badge-title">TOTAL SMILE</div><div class="badge-sub">PERIODONTAL</div>
    <div class="badge-price">$89</div><div class="badge-per">/MONTH</div>
  </div>
  <div class="price-pill" style="left:439px;top:571px">$89/MONTH</div>

  <!-- Join band -->
  <section class="join">
    <div class="join-title">JOIN SMILE CLUB TODAY!</div>
    <svg class="phone-icon" viewBox="0 0 28 28" aria-hidden="true"><circle cx="14" cy="14" r="14" fill="var(--green)"/><path d="M10 7.5c.6-.4 1.3-.2 1.6.4l1.2 2.3c.3.6.1 1.2-.4 1.5l-.9.6c.6 1.6 1.8 3 3.3 3.9l.7-.8c.4-.5 1.1-.6 1.6-.2l2.1 1.5c.5.4.6 1.1.2 1.6l-.9 1.1c-.6.7-1.6 1-2.5.7-4.1-1.5-7.200-5.1-8-9.4-.2-.9.2-1.8 1-2.3z" fill="#fff"/></svg>
    <div class="join-phone">865-555-0142</div>
  </section>

  <!-- New Smile offer -->
  <section class="offer-card">
    <ul class="features">
      <li><svg viewBox="0 0 12 12"><circle cx="6" cy="6" r="6" fill="#9bde4d"/><path d="M3.2 6.2l1.9 1.8 3.7-3.8" stroke="#fff" stroke-width="1.6" fill="none"/></svg>Cleaning + Comprehensive Exam + Whitening</li>
    </ul>
  </section>
  <svg class="arc" style="left:425px;top:610px" viewBox="0 0 170 62" aria-hidden="true"><path d="M13,55 A78,78 0 0 1 157,55" stroke="var(--green)" stroke-width="2" fill="none"/><circle cx="13" cy="55" r="3.5" fill="var(--green)"/><circle cx="157" cy="55" r="3.5" fill="var(--green)"/></svg>
  <div class="badge" style="left:440px;top:625px">
    <div class="badge-new">New</div>
    <div class="badge-smile">SMILE</div>
    <div class="badge-sub">REFRESH PACKAGE</div>
    <div class="badge-price">$499</div>
  </div>
  <div class="pill offer-pill">LIMITED TIME OFFER</div>

  <!-- Financing -->
  <div class="finance-title">FLEXIBLE FINANCING FOR TREATMENT:</div>
  <div class="partner partner-a"><span class="dot"></span>Orvane Pay</div>
  <div class="partner partner-b"><span class="dot"></span>Tellory Finance</div>
  <div class="plans">PAYMENT PLANS AVAILABLE</div>

  <svg class="fee-band" viewBox="0 0 627 30" aria-hidden="true"><path d="M245,0 L627,0 L627,30 L217,30 Z" fill="var(--green)"/></svg>
  <div class="fee-text">*$49 Lifetime Activation Fee (Non-Refundable)</div>
</main>
</body>
</html>
```